Lanterns After Rain - CD cover indie music

This is my 4th and final album. I am sharing my story of trials, pain and persistence that led me here, like a sound track to a short film.
I would like a design that communicates both a painful phase of life, yet tranquility and beauty found as life winds down. Can be illustrated or photograph.
On front design should have title 'Lanterns After Rain' and artist name.
I will need to add credits and song list.
I am thinking a booklet will be added with lyrics and a few photos and plan to work with this artist. Thank you

Target Market(s)

Folk, easy listening, story telling

Industry/Entity Type

Indie music - independent

Font styles to use
Sans Serif
Other font styles liked:
• I like also verdana font.

Requirements
Nice to have
• a contrast of colors to emotions may work well. There is a portuguese word ‘saudade’ that expresses sadness, but longing also.
Should not have
• No bright red. Not busy. No images of people or animals.

```html
<!DOCTYPE html>
<html lang="en">
<head>
<meta charset="utf-8">
<title>Lanterns After Rain – Album Cover</title>
<link rel="stylesheet" href="https://fonts.googleapis.com/css2?family=Lexend:wght@700;800&family=Audiowide&display=swap">
<style>
  :root {
    --canvas-bg: #ffffff;
    --paper: #d6d6d6;
    --paper-light: #e2e2e2;
    --burn-edge: #2b2824;
    --sky-top: #0e3b3d;
    --sky-mid: #3b4d57;
    --dusk: #8a5a4c;
    --horizon: #c2592e;
    --water: #4a2a22;
    --water-deep: #171210;
    --title-white: #f4f4f4;
    --title-gold: #f5b319;
    --title-shadow: rgba(40, 20, 10, 0.75);
  }
  html, body {
    margin: 0;
    padding: 0;
    width: 1200px;
    height: 1000px;
    overflow: hidden;
    background: var(--canvas-bg);
  }
  .cover {
    position: relative;
    width: 1200px;
    height: 1000px;
  }
  .cover-art {
    position: absolute;
    inset: 0;
  }
  .cover-title {
    position: absolute;
    left: 0;
    width: 1170px;
    text-align: center;
    margin: 0;
    font-family: "Lexend", "Verdana", sans-serif;
    text-transform: uppercase;
    line-height: 1;
  }
  .title-line-top {
    top: 452px;
    font-size: 52px;
    font-weight: 700;
    letter-spacing: 2px;
    color: var(--title-white);
    text-shadow: 3px 4px 0 var(--title-shadow);
  }
  .title-line-main {
    top: 526px;
    font-size: 86px;
    font-weight: 800;
    letter-spacing: 3px;
    color: var(--title-gold);
    text-shadow: 4px 5px 0 var(--title-shadow);
  }
  .artist-name {
    position: absolute;
    top: 676px;
    left: 0;
    width: 1174px;
    text-align: center;
    margin: 0;
    font-family: "Audiowide", "Verdana", sans-serif;
    font-size: 34px;
    color: var(--title-white);
    letter-spacing: 1px;
  }
</style>
</head>
<body>
<main class="cover">
  <svg class="cover-art" width="1200" height="1000" viewBox="0 0 1200 1000" xmlns="http://www.w3.org/2000/svg">
    <defs>
      <linearGradient id="paperTone" x1="0" y1="0" x2="1" y2="1">
        <stop offset="0" stop-color="var(--paper-light)"/>
        <stop offset="1" stop-color="var(--paper)"/>
      </linearGradient>
      <linearGradient id="duskScene" x1="0" y1="0" x2="0" y2="1">
        <stop offset="0" stop-color="var(--sky-top)"/>
        <stop offset="0.35" stop-color="var(--sky-mid)"/>
        <stop offset="0.55" stop-color="var(--dusk)"/>
        <stop offset="0.68" stop-color="var(--horizon)"/>
        <stop offset="0.72" stop-color="var(--water)"/>
        <stop offset="1" stop-color="var(--water-deep)"/>
      </linearGradient>
      <filter id="burnBlur" x="-10%" y="-10%" width="120%" height="120%">
        <feGaussianBlur stdDeviation="4"/>
      </filter>
    </defs>

    <rect class="paper-sheet" x="112" y="12" width="976" height="976" fill="url(#paperTone)"/>

    <path class="torn-edge" filter="url(#burnBlur)" fill="none" stroke="var(--burn-edge)" stroke-width="12"
      d="M300 135 L420 90 L520 70 L640 50 L700 35 L780 55 L835 70 L845 170 L870 260 L930 370 L960 460 L990 560 L985 690 L972 770 L990 988 L392 988 L340 880 L300 790 L255 700 L205 590 L160 470 L145 380 L170 300 L215 240 L255 180 Z"/>

    <path class="scene-window" role="img" aria-label="Photograph of a quiet shoreline at dusk under a starry teal sky, the low sun glowing orange over still reflective water"
      fill="url(#duskScene)"
      d="M300 135 L420 90 L520 70 L640 50 L700 35 L780 55 L835 70 L845 170 L870 260 L930 370 L960 460 L990 560 L985 690 L972 770 L990 988 L392 988 L340 880 L300 790 L255 700 L205 590 L160 470 L145 380 L170 300 L215 240 L255 180 Z"/>
  </svg>

  <h1>
    <span class="cover-title title-line-top">Lanterns After</span>
    <span class="cover-title title-line-main">Rain</span>
  </h1>
  <p class="artist-name">ARTIST NAME</p>
</main>
</body>
</html>
```